Pine Fox truck design

Hi there, i am looking to take my design onto our trucks. I have a basis of design, just not happy with it yet. It needs to feel vintage, fun, have a reason to call as well as showcase our brand. Our brand needs some help. The words id like on the truck are
Moving
Packing
Storage
Cleaning
Long Haul Moves
Estate Auction Sales
Local Dorvik Agent
Junk Removal
Donation Runs
Receiving
Inspections
Deliveries
Pick ups

I like the truck design so far, but just feels lacking. See images labeled truck.

These are for a 16' box truck. If you follow sizes of the truck design, I can manipulate after. thank you,,

```html
<!DOCTYPE html>
<html lang="en">
<head>
<meta charset="utf-8">
<title>Pine Fox Moving &amp; Storage – Truck Side Panel</title>
<link rel="stylesheet" href="https://fonts.googleapis.com/css2?family=Josefin+Sans:wght@600;700&display=swap">
<style>
  :root {
    --navy: #1d1877;
    --pink: #ef2a5d;
    --pink-deep: #e01f52;
    --pink-light: #ff4f80;
    --chevron: #ff3f72;
    --white: #ffffff;
    --gold: #c99a2e;
    --gold-light: #f2d27a;
  }
  * { box-sizing: border-box; margin: 0; padding: 0; }
  html, body { width: 1200px; height: 1000px; overflow: hidden; background: var(--white); }
  body { position: relative; font-family: "Josefin Sans", "Futura", sans-serif; }

  .truck-panel {
    position: absolute; left: 14px; top: 272px; width: 1173px; height: 455px;
    background: radial-gradient(circle at 50% 45%, var(--pink-light) 0%, var(--pink) 45%, var(--pink-deep) 100%);
    overflow: hidden;
  }

  .service-list {
    position: absolute; left: 16px; top: 20px; width: 455px;
    display: flex; flex-direction: column; gap: 11px;
  }
  .service-row { display: flex; gap: 9px; }
  .service {
    height: 36px; display: flex; align-items: center;
    padding: 4px 16px 0 17px; gap: 10px;
    background: var(--navy); color: var(--white);
    border-radius: 9px; outline: 1.5px dashed rgba(255,255,255,.8); outline-offset: -4px;
    font-weight: 700; font-size: 22px; letter-spacing: .2px; white-space: nowrap;
  }
  .service.short { min-width: 198px; }
  .service svg { width: 22px; height: 16px; margin-top: -4px; flex: none; }

  .mascot {
    position: absolute; left: 478px; top: 18px; width: 216px; height: 216px; border-radius: 50%;
    background: radial-gradient(circle at 50% 40%, #ffffff 0%, #f4f3fb 60%, #d9d6ef 100%);
  }

  .brand-name {
    position: absolute; left: 396px; top: 228px; width: 380px; text-align: center;
    color: var(--navy); font-weight: 700; font-size: 58px; letter-spacing: 1px; line-height: 1;
  }
  .brand-tagline {
    position: absolute; left: 396px; top: 280px; width: 380px; text-align: center;
    color: var(--navy); font-weight: 700; font-size: 20px; letter-spacing: 1px;
  }

  .sign {
    position: absolute; left: 790px; top: 38px; width: 350px; height: 220px;
    background: var(--navy); border-radius: 22px; transform: rotate(-8deg);
    display: flex; align-items: center; justify-content: center; text-align: center;
  }
  .sign::before {
    content: ""; position: absolute; inset: 10px; border: 2px dotted var(--pink-light); border-radius: 16px;
  }
  .sign-text { color: var(--white); font-weight: 700; line-height: 1.1; }
  .sign-text .small { display: block; font-size: 26px; }
  .sign-text .big { display: block; font-size: 34px; }
  .sign-strings { position: absolute; left: 840px; top: 0; width: 200px; height: 100px; }

  .badge-seal {
    position: absolute; left: 470px; top: 330px; width: 110px; height: 110px; border-radius: 50%;
    background: radial-gradient(circle, var(--gold-light) 0%, var(--gold) 70%, #8d6a17 100%);
  }
  .owner-signature {
    position: absolute; left: 590px; top: 352px; width: 160px; height: 86px; border-radius: 8px;
    background: linear-gradient(90deg, rgba(255,255,255,.22), rgba(255,255,255,.1));
  }
  .number-badge {
    position: absolute; left: 756px; top: 362px; width: 32px; height: 32px; border-radius: 50%;
    background: var(--white);
  }

  .phone-icon { position: absolute; left: 1092px; top: 310px; width: 40px; height: 36px; }
  .call-line {
    position: absolute; right: 28px; top: 360px; color: var(--white);
    font-weight: 700; font-size: 22px; letter-spacing: .3px;
  }
  .phone-number {
    position: absolute; right: 28px; top: 386px; color: var(--white);
    font-weight: 700; font-size: 48px; letter-spacing: 1px;
  }
</style>
</head>
<body>
<main class="truck-panel">
  <svg width="0" height="0" style="position:absolute">
    <defs>
      <symbol id="chevrons" viewBox="0 0 22 16">
        <path d="M1 1 L8 8 L1 15" fill="none" stroke="#ff3f72" stroke-width="3.5"/>
        <path d="M11 1 L18 8 L11 15" fill="none" stroke="#ff3f72" stroke-width="3.5"/>
      </symbol>
    </defs>
  </svg>

  <div class="service-list">
    <div class="service-row">
      <div class="service short"><svg><use href="#chevrons"/></svg>MOVING</div>
      <div class="service short"><svg><use href="#chevrons"/></svg>PACKING</div>
    </div>
    <div class="service-row">
      <div class="service short"><svg><use href="#chevrons"/></svg>STORAGE</div>
      <div class="service short"><svg><use href="#chevrons"/></svg>CLEANING</div>
    </div>
    <div class="service-row"><div class="service"><svg><use href="#chevrons"/></svg>LONG HAUL MOVES</div></div>
    <div class="service-row"><div class="service"><svg><use href="#chevrons"/></svg>ESTATE AUCTION SALES</div></div>
    <div class="service-row"><div class="service"><svg><use href="#chevrons"/></svg>LOCAL DORVIK AGENT</div></div>
    <div class="service-row"><div class="service"><svg><use href="#chevrons"/></svg>JUNK REMOVAL</div></div>
    <div class="service-row"><div class="service"><svg><use href="#chevrons"/></svg>DONATION RUNS</div></div>
    <div class="service-row">
      <div class="service"><svg><use href="#chevrons"/></svg>RECEIVING</div>
      <div class="service"><svg><use href="#chevrons"/></svg>INSPECTIONS</div>
    </div>
    <div class="service-row">
      <div class="service"><svg><use href="#chevrons"/></svg>DELIVERIES</div>
      <div class="service"><svg><use href="#chevrons"/></svg>PICK UPS</div>
    </div>
  </div>

  <div class="mascot" role="img" aria-label="Vintage illustration of a smiling operator on a retro telephone"></div>
  <div class="brand-name">PINE FOX</div>
  <div class="brand-tagline">MOVING &amp; STORAGE</div>

  <div class="sign">
    <p class="sign-text"><span class="small">OPERATORS</span><span class="big">STANDING BY!</span></p>
  </div>
  <svg class="sign-strings" viewBox="0 0 200 100" aria-hidden="true">
    <line x1="40" y1="0" x2="38" y2="69" stroke="#fff" stroke-width="2"/>
    <line x1="158" y1="0" x2="162" y2="52" stroke="#fff" stroke-width="2"/>
    <circle cx="38" cy="69" r="5" fill="#ff3f72"/>
    <circle cx="162" cy="52" r="5" fill="#ff3f72"/>
  </svg>

  <div class="badge-seal" role="img" aria-label="Women-owned business certification seal"></div>
  <div class="owner-signature" role="img" aria-label="Owner's handwritten signature"></div>
  <div class="number-badge"></div>

  <svg class="phone-icon" viewBox="0 0 40 36" aria-hidden="true">
    <path d="M2 12 C6 2 34 2 38 12 L38 15 L30 15 L28 10 L12 10 L10 15 L2 15 Z" fill="#fff"/>
    <path d="M9 16 L31 16 L36 34 L4 34 Z" fill="#fff"/>
    <g fill="#ef2a5d">
      <rect x="13" y="21" width="3" height="3"/><rect x="18.5" y="21" width="3" height="3"/><rect x="24" y="21" width="3" height="3"/>
      <rect x="13" y="27" width="3" height="3"/><rect x="18.5" y="27" width="3" height="3"/><rect x="24" y="27" width="3" height="3"/>
    </g>
  </svg>
  <p class="call-line">PINE FOX AT YOUR SERVICE</p>
  <p class="phone-number">970-555-0148</p>
</main>
</body>
</html>
```